Create intro for YouTube Channel on Motorcycle Travel and General Travel worldwide

Easily usable with Adobe Premier Pro for travel and motorcycle videos. Need to have an intro animated design and a standard end design clips for both Motorcycle Videos and General Travel Videos.

Requirements
Must have
• Animation on the intros and ending's
Nice to have
• For the general travel video a world with a plane circling for the motorcycle something similar.

```html
<!DOCTYPE html>
<html lang="en">
<head>
<meta charset="utf-8">
<title>Roamwheel – End Screen</title>
<link rel="stylesheet" href="https://fonts.googleapis.com/css2?family=Poppins:wght@500;600&display=swap">
<style>
  :root {
    --sky-top: #d9dadb;
    --sky-haze: #dcd8cf;
    --road-mid: #cbc4b4;
    --road-low: #bfb8a8;
    --accent-red: #ee3d33;
    --panel-dark: #404043;
    --ink: #363638;
    --ink-soft: #3f3f42;
  }
  * { margin: 0; padding: 0; box-sizing: border-box; }
  html, body {
    width: 1200px;
    height: 595px;
    overflow: hidden;
    background: var(--sky-top);
  }
  .end-screen {
    position: relative;
    width: 1200px;
    height: 595px;
    overflow: hidden;
    font-family: "Poppins", sans-serif;
  }
  .backdrop-footage {
    position: absolute;
    inset: 0;
    background: linear-gradient(180deg,
      var(--sky-top) 0%,
      var(--sky-haze) 45%,
      var(--road-mid) 62%,
      var(--road-low) 100%);
  }
  .video-slot {
    position: absolute;
    top: 190px;
    width: 384px;
    height: 215px;
  }
  .video-slot--recommended { left: 29px; background: var(--accent-red); }
  .video-slot--next { left: 784px; background: var(--panel-dark); }
  .slot-label {
    position: absolute;
    top: 155px;
    width: 384px;
    text-align: center;
    font-size: 19px;
    font-weight: 500;
    letter-spacing: 0.2px;
    color: var(--ink);
  }
  .slot-label--recommended { left: 29px; }
  .slot-label--next { left: 784px; color: #1f1f21; }
  .channel-name {
    position: absolute;
    left: 436px;
    top: 270px;
    width: 320px;
    display: flex;
    align-items: center;
    justify-content: center;
    gap: 12px;
    font-size: 38px;
    font-weight: 600;
    color: var(--ink-soft);
  }
  .channel-dot {
    width: 22px;
    height: 22px;
    border-radius: 50%;
    background: var(--accent-red);
    flex: none;
  }
  .call-to-action {
    position: absolute;
    left: 0;
    top: 497px;
    width: 1194px;
    display: flex;
    justify-content: center;
    gap: 36px;
    font-size: 34px;
    font-weight: 600;
    color: var(--ink-soft);
    list-style: none;
  }
</style>
</head>
<body>
  <main class="end-screen">
    <div class="backdrop-footage" role="img" aria-label="Faded video footage of an open highway stretching toward hills under a hazy sky"></div>

    <p class="slot-label slot-label--recommended">RECOMMENDED VIDEO</p>
    <div class="video-slot video-slot--recommended"></div>

    <div class="channel-name">
      <span class="channel-dot"></span>
      <span>Roamwheel</span>
    </div>

    <p class="slot-label slot-label--next">NEXT VIDEO</p>
    <div class="video-slot video-slot--next"></div>

    <ul class="call-to-action">
      <li>LIKE</li>
      <li>SUBSCRIBE</li>
      <li>SHARE</li>
    </ul>
  </main>
</body>
</html>
```